New business card for civil engineering company - "Keystone Audit"

We need a business card designed for our new structural engineering company.

The company name is "Keystone Audit" logo files attached.

We would like the following:
* Two-sided card
* Simple design

Information to be placed on the card:
Name - Marcus Dellow
Job Title - Director / Structural Engineer
Credentials - BEng(Hons), CPEng, CMengNZ, IntPE(NZ)
Email - marcus.dellow@keystoneaudit.co.nz
mobile - 0219364058
website - www.keystoneaudit.co.nz

```html
<!DOCTYPE html>
<html lang="en">
<head>
<meta charset="utf-8">
<title>Keystone Audit – Business Card</title>
<link rel="stylesheet" href="https://fonts.googleapis.com/css2?family=Arimo:wght@400;700&display=swap">
<style>
  :root {
    --backdrop: #ececec;
    --card: #ffffff;
    --ink: #2f3136;
    --ink-soft: #7a7c80;
    --accent: #2f6fc4;
    --tint-from: #c4d3ef;
    --tint-to: #e6eefa;
    --rule: #c9cacd;
  }
  * { box-sizing: border-box; margin: 0; padding: 0; }
  html, body {
    width: 1200px;
    height: 800px;
    overflow: hidden;
    background: var(--backdrop);
    font-family: "Arimo", Arial, sans-serif;
  }
  .canvas { position: relative; width: 1200px; height: 800px; }

  .card {
    position: absolute;
    width: 560px;
    height: 311px;
    background: var(--card);
    box-shadow: 0 6px 18px rgba(0,0,0,0.12);
    overflow: hidden;
  }
  .card--front { left: 110px; top: 70px; }
  .card--back  { left: 530px; top: 420px; }

  .wordmark {
    display: flex;
    align-items: center;
    gap: 8px;
    font-weight: 700;
    color: var(--ink);
    white-space: nowrap;
    letter-spacing: 1px;
  }
  .wordmark__square { background: var(--accent); flex: none; }

  /* Front */
  .front-band {
    position: absolute;
    left: 0;
    right: 0;
    bottom: 0;
    height: 18px;
    background: linear-gradient(90deg, var(--tint-from), var(--tint-to));
  }
  .card--front .wordmark {
    position: absolute;
    left: 50%;
    top: 50%;
    transform: translate(-50%, -50%);
    font-size: 20px;
  }
  .card--front .wordmark__square { width: 10px; height: 10px; }

  /* Back */
  .brand-block {
    position: absolute;
    left: 30px;
    top: 0;
    width: 190px;
    height: 100%;
    display: flex;
    align-items: center;
    justify-content: center;
  }
  .brand-block .wordmark { font-size: 13px; gap: 6px; }
  .brand-block .wordmark__square { width: 8px; height: 8px; }
  .divider {
    position: absolute;
    left: 232px;
    top: 100px;
    width: 1px;
    height: 120px;
    background: var(--rule);
  }
  .details {
    position: absolute;
    left: 256px;
    top: 72px;
    width: 290px;
    color: var(--ink-soft);
  }
  .details__name { font-size: 24px; font-weight: 400; margin-bottom: 6px; }
  .details__role { font-size: 13px; line-height: 1.45; }
  .details__creds { font-size: 12px; line-height: 1.45; margin-bottom: 10px; }
  .contact { list-style: none; }
  .contact__item {
    display: flex;
    align-items: center;
    gap: 8px;
    font-size: 12px;
    line-height: 1.9;
  }
  .contact__icon { width: 12px; height: 12px; flex: none; }
</style>
</head>
<body>
<main class="canvas">

  <section class="card card--front" aria-label="Card front">
    <div class="front-band" role="img" aria-label="Pale blue decorative band"></div>
    <div class="wordmark">
      <span class="wordmark__square"></span>
      <span class="wordmark__name">KEYSTONE AUDIT</span>
    </div>
  </section>

  <section class="card card--back" aria-label="Card back">
    <div class="brand-block">
      <div class="wordmark">
        <span class="wordmark__square"></span>
        <span class="wordmark__name">KEYSTONE AUDIT</span>
      </div>
    </div>
    <div class="divider"></div>
    <div class="details">
      <h1 class="details__name">Marcus Dellow</h1>
      <p class="details__role">Director / Structural Engineer</p>
      <p class="details__creds">BEng(Hons), CPEng, CMengNZ, IntPE(NZ)</p>
      <ul class="contact">
        <li class="contact__item">
          <svg class="contact__icon" viewBox="0 0 12 12" aria-hidden="true">
            <rect x="3" y="0.8" width="6" height="10.4" rx="1.2" fill="none" stroke="var(--accent)" stroke-width="1.3"/>
            <circle cx="6" cy="9.3" r="0.7" fill="var(--accent)"/>
          </svg>
          <span>0219364058</span>
        </li>
        <li class="contact__item">
          <svg class="contact__icon" viewBox="0 0 12 12" aria-hidden="true">
            <rect x="0.5" y="2.5" width="11" height="7.5" fill="var(--accent)"/>
            <polyline points="0.8,3 6,7 11.2,3" fill="none" stroke="#fff" stroke-width="1"/>
          </svg>
          <span>marcus.dellow@keystoneaudit.co.nz</span>
        </li>
        <li class="contact__item">
          <svg class="contact__icon" viewBox="0 0 12 12" aria-hidden="true">
            <circle cx="6" cy="6" r="5.5" fill="var(--accent)"/>
            <ellipse cx="6" cy="6" rx="2.3" ry="5.3" fill="none" stroke="#fff" stroke-width="0.8"/>
            <line x1="0.6" y1="6" x2="11.4" y2="6" stroke="#fff" stroke-width="0.8"/>
          </svg>
          <span>www.keystoneaudit.co.nz</span>
        </li>
      </ul>
    </div>
  </section>

</main>
</body>
</html>
```